Crestmoor Business Cards

I need a business card designed with the following information.

Company Name: Crestmoor Wealth Management
Name: BriAnne Tolvey
Title: Executive Assistant
Cell: (555) 302-7164
Direct Line: (555) 917-5082
Email: brianne@crestmoorwm.example
Address: 20537 W. Harwell PKWY Ste. B
Brinwood, TX 77512

I have attached the logo.
I would like it in navy blue and silver.
Thanks.

```html
<!DOCTYPE html>
<html lang="en">
<head>
<meta charset="utf-8">
<title>Crestmoor Wealth Management – Business Cards</title>
<link rel="stylesheet" href="https://fonts.googleapis.com/css2?family=Montserrat:wght@400;500;600&display=swap">
<style>
  :root {
    --navy: #10244a;
    --navy-deep: #0d1f40;
    --silver: #c9ccd2;
    --paper: #ffffff;
    --ink: #1a2a4c;
    --stage: #e6e7ea;
  }
  * { box-sizing: border-box; margin: 0; padding: 0; }
  html, body { width: 1200px; height: 1000px; overflow: hidden; }
  body {
    background: var(--stage);
    font-family: "Montserrat", Arial, sans-serif;
    position: relative;
  }
  .card {
    position: absolute;
    width: 700px;
    height: 400px;
    box-shadow: 0 6px 18px rgba(0,0,0,.18);
  }
  .card--front { left: 140px; top: 90px; background: var(--navy-deep); }
  .card--back { left: 360px; top: 510px; background: var(--paper); color: var(--ink); }

  .wordmark { display: flex; align-items: center; gap: 14px; font-weight: 500; }
  .wordmark__square { width: 26px; height: 26px; flex: none; }
  .wordmark__name { font-size: 30px; letter-spacing: 10px; line-height: 1; white-space: nowrap; }
  .wordmark__tag { font-size: 10px; letter-spacing: 3.2px; margin-top: 8px; white-space: nowrap; }

  .card--front .wordmark { position: absolute; right: 60px; top: 180px; color: var(--paper); }
  .card--front .wordmark__square { background: var(--silver); }

  .card--back .wordmark { position: absolute; left: 70px; top: 110px; color: var(--navy); }
  .card--back .wordmark__square { background: var(--navy); }

  .person {
    position: absolute;
    left: 180px; top: 260px;
    padding-left: 16px;
    border-left: 2px solid var(--navy);
  }
  .person__name { font-size: 20px; font-weight: 600; color: var(--navy); white-space: nowrap; }
  .person__title { font-size: 12px; margin-top: 4px; white-space: nowrap; }
  .person__address { font-size: 12px; line-height: 1.55; margin-top: 18px; white-space: nowrap; }

  .contact {
    position: absolute;
    left: 470px; top: 262px;
    list-style: none;
    font-size: 12px;
    line-height: 1.7;
  }
  .contact li { display: flex; align-items: center; gap: 6px; white-space: nowrap; }
  .contact svg { width: 11px; height: 11px; fill: var(--navy); flex: none; }
</style>
</head>
<body>
  <section class="card card--front" aria-label="Card front">
    <div class="wordmark">
      <span class="wordmark__square"></span>
      <div>
        <div class="wordmark__name">CRESTMOOR</div>
        <div class="wordmark__tag">WEALTH MANAGEMENT</div>
      </div>
    </div>
  </section>

  <section class="card card--back" aria-label="Card back">
    <div class="wordmark">
      <span class="wordmark__square"></span>
      <div>
        <div class="wordmark__name">CRESTMOOR</div>
        <div class="wordmark__tag">WEALTH MANAGEMENT</div>
      </div>
    </div>

    <div class="person">
      <div class="person__name">BriAnne Tolvey</div>
      <div class="person__title">Executive Assistant</div>
      <div class="person__address">20537 W. Harwell PKWY Ste. B<br>Brinwood, TX 77512</div>
    </div>

    <ul class="contact">
      <li>
        <svg viewBox="0 0 12 12" aria-hidden="true"><path d="M2.5 1l2 2.2-1 1.3c.7 1.5 1.8 2.6 3.3 3.3l1.3-1 2.2 2-1.2 1.7C5.3 10.3 1.7 6.7 1 2.1z"/></svg>
        Direct Line: (555) 917-5082
      </li>
      <li>
        <svg viewBox="0 0 12 12" aria-hidden="true"><path d="M3 0.5h6v11H3zM4 1.8v7.4h4V1.8z"/></svg>
        (555) 302-7164
      </li>
      <li>
        <svg viewBox="0 0 12 12" aria-hidden="true"><path d="M0.5 2.5h11v7h-11zM1.5 3.3L6 6.6l4.5-3.3z"/></svg>
        brianne@crestmoorwm.example
      </li>
    </ul>
  </section>
</body>
</html>
```